Fitness retail site needs YS page design

I need to update my Yarnspot page to present a professional appearance. I'm open to any colors, except pink. I would like the colors to coordinate with the logo. I added yellow, but not really necessary to include, just put it out there as an idea. i included pictures of the products I will be selling. Include the words BIKINI, FIGURE, FITNESS, BODYBUILDING, PHYSIQUE.

Target Market(s)

Women fitness competitors

Industry/Entity Type

Fitness

Font styles to use
Serif

Colors
ec1f27
ffffff
919191
1b1b1b
fbf289

Requirements
Must have
• Professional, not homemade appearance. Eye catching, not too busy.. Pictures are not compulsory, just added for ideas. Use them or not.
Should not have
• Pictures of people working out or holding weights. No pink or princess type designs

```html
<!DOCTYPE html>
<html lang="en">
<head>
<meta charset="utf-8">
<title>Competition Essentials</title>
<link href="https://fonts.googleapis.com/css2?family=Roboto:ital,wght@1,500&display=swap" rel="stylesheet">
<style>
  :root {
    --orange: #fd9a35;
    --panel: #ececec;
    --ink: #4d4d4d;
    --accent: #ec1f27;
    --product-dark: #2a2a2a;
    --product-mid: #3a3a3a;
  }
  html, body {
    margin: 0;
    padding: 0;
    overflow: hidden;
  }
  .banner {
    position: relative;
    width: 1200px;
    height: 457px;
    background: var(--orange);
    overflow: hidden;
    font-family: "Roboto", Arial, sans-serif;
  }
  .category-panel {
    position: absolute;
    inset: 0;
    width: 1200px;
    height: 457px;
  }
  .product {
    position: absolute;
  }
  .product--lotions {
    left: 26px;
    top: 139px;
    width: 147px;
    height: 195px;
    border-radius: 14px 14px 6px 6px;
    background: linear-gradient(90deg, var(--product-dark), var(--product-mid) 50%, var(--product-dark));
  }
  .product--corset {
    left: 212px;
    top: 117px;
    width: 212px;
    height: 220px;
    border-radius: 30px;
    background: linear-gradient(90deg, #222, var(--product-mid) 50%, #222);
  }
  .product--sandals {
    left: 461px;
    top: 124px;
    width: 278px;
    height: 206px;
    border-radius: 40px;
    background: linear-gradient(100deg, #1f1f1f, #5a3a26 35%, #3a2a30 65%, #2e2e2e);
  }
  .category-list {
    position: absolute;
    left: 0;
    top: 0;
    margin: 0;
    padding: 0;
    list-style: none;
  }
  .category {
    position: absolute;
    white-space: nowrap;
    font-size: 35px;
    font-style: italic;
    font-weight: 500;
    color: var(--ink);
    line-height: 1;
    letter-spacing: 0.5px;
  }
  .category::before {
    content: ">";
    position: absolute;
    left: -28px;
    top: 6px;
    font-size: 22px;
    font-style: normal;
    font-weight: 500;
    color: var(--accent);
  }
  .category--bikini { left: 888px; top: 108px; }
  .category--figure { left: 879px; top: 160px; }
  .category--fitness { left: 869px; top: 213px; }
  .category--bodybuilding { left: 860px; top: 265px; }
  .category--physique { left: 850px; top: 316px; }
</style>
</head>
<body>
<main class="banner">
  <svg class="category-panel" viewBox="0 0 1200 457" aria-hidden="true">
    <polygon points="834,0 1200,0 1200,457 754,457" fill="var(--panel)"/>
  </svg>

  <div class="product product--lotions" role="img" aria-label="Two black bottles of competition tanning lotion"></div>
  <div class="product product--corset" role="img" aria-label="Black waist trainer corset with hook closures"></div>
  <div class="product product--sandals" role="img" aria-label="Four pairs of rhinestone strap flip-flops in black, brown and grey"></div>

  <ul class="category-list">
    <li class="category category--bikini">BIKINI</li>
    <li class="category category--figure">FIGURE</li>
    <li class="category category--fitness">FITNESS</li>
    <li class="category category--bodybuilding">BODYBUILDING</li>
    <li class="category category--physique">PHYSIQUE</li>
  </ul>
</main>
</body>
</html>
```